Mira Lune Window Decals

I need a design for a full set of shop front of window decals. The window and door combined are approximately 3.3m long by 2.38 meters tall, The glass door to one side (attached is a sketch with dimensions - looking from the outside)

Mira Lune is a beauty and massage therapy center that has a balanced mix of business in terms of male and female clients. The business provides traditional foot massage, body massage, seated neck and shoulder massage and a full range of facial skin care services - its basically a combination of day spa and foot massage center.

The store reception desk and retail displays are directly behind the window so I'd like some vision in but also some degree of screening from the bright sun here in Singapore.

Inclusion of a space for a digital photoframe would allow me to play promotions and product detail to the passing traffic (the shop unit is directly opposite a busy shopping mall

I need the design to really state what services are offered and to look gender neutral to ensure male guests are not alienated.

The overall look should lean towards contemporary/modern styling.

Competition is quite considerable in this location with a 'Velnorita' branded beauty salon occupying the unit directly adjacent on the right side.

The idea is that the decals will be printed and installed to the inside of the glass to extend the life and reduce fading

The name of the Business is currently mira lune, however there is no need to include this in the design as there is a sing box above the window (redesigning that signage/logo will be my next project)

I've included a picture of the existing shop front - its pretty woeful.. we only recently purchased the business and need to make a lot of changes... starting with the window... right

Thanks

Tobin
Updates

Project Deadline Extended
Reason: I have extended the deadline as the invitation was accepted by many designers who have yet to submit initial designs Thanks you all for you hard work and effort

Target Market(s)

Male and Female Asian and Expatriate 25-65 years old professionals

Industry/Entity Type

Beauty Salon

Font styles to use
Serif
Sans Serif

Requirements
Must have
• eye catching, and illustrate what we do do
space for digital photo frame (closest power is to the right)
Should not have
• must not look overly femine

```html
<!DOCTYPE html>
<html lang="en">
<head>
<meta charset="utf-8">
<title>Mira Lune Beauty Center – Window Decals</title>
<link rel="stylesheet" href="https://fonts.googleapis.com/css2?family=Nunito:wght@700;800&family=Arimo&display=swap">
<style>
  :root {
    --glass-top: #e9dfdf;
    --glass-mid: #d9d4cc;
    --glass-bottom: #ccceb6;
    --mullion: #ffffff;
    --olive: #727a58;
    --olive-soft: rgba(114, 122, 88, 0.55);
    --frame-light: #dcd5c0;
    --frame-dark: #b9b09f;
    --decal-line: rgba(255, 255, 255, 0.75);
  }
  html, body {
    margin: 0;
    padding: 0;
    width: 1200px;
    height: 1000px;
    overflow: hidden;
  }
  .shopfront {
    position: relative;
    width: 1200px;
    height: 1000px;
    background: linear-gradient(180deg, var(--glass-top) 0%, var(--glass-mid) 55%, var(--glass-bottom) 100%);
    font-family: "Nunito", sans-serif;
  }
  .mullion {
    position: absolute;
    top: 0;
    height: 1000px;
    background: var(--mullion);
  }
  .mullion--left { left: 75px; width: 10px; }
  .mullion--right { left: 492px; width: 6px; }
  .side-glass {
    position: absolute;
    left: 0; top: 0;
    width: 75px; height: 1000px;
    background: linear-gradient(90deg, rgba(255,255,255,0.15), rgba(0,0,0,0.03));
  }
  .door-lines {
    position: absolute;
    left: 85px; top: 0;
    width: 407px; height: 1000px;
  }
  .brand {
    position: absolute;
    left: 85px;
    top: 578px;
    width: 410px;
    text-align: center;
    color: var(--olive);
    font-weight: 700;
    font-size: 31px;
    line-height: 42px;
    margin: 0;
  }
  .photo-frame {
    position: absolute;
    left: 535px; top: 69px;
    width: 312px; height: 172px;
    background: radial-gradient(ellipse at 50% 40%, var(--frame-light) 35%, var(--frame-dark) 100%);
    display: flex;
    align-items: center;
    justify-content: center;
    font-family: "Arimo", sans-serif;
    font-size: 20px;
    color: #ffffff;
    white-space: nowrap;
  }
  .ornament {
    position: absolute;
    left: 660px; top: 180px;
    width: 540px; height: 820px;
    background: radial-gradient(ellipse at 65% 55%, var(--olive-soft) 0%, rgba(114,122,88,0.25) 45%, rgba(114,122,88,0) 72%);
  }
  .services {
    position: absolute;
    left: 535px; top: 660px;
    margin: 0; padding: 0;
    list-style: none;
    color: var(--olive);
    font-weight: 700;
    font-size: 24px;
    line-height: 31.2px;
  }
  .phone {
    position: absolute;
    left: 535px; top: 926px;
    margin: 0;
    color: var(--olive);
    font-weight: 800;
    font-size: 39px;
  }
</style>
</head>
<body>
<main class="shopfront">
  <div class="side-glass"></div>
  <div class="mullion mullion--left"></div>
  <div class="mullion mullion--right"></div>

  <svg class="door-lines" viewBox="0 0 407 1000" aria-hidden="true">
    <g stroke="var(--decal-line)" stroke-width="6" fill="none">
      <line x1="0" y1="41" x2="407" y2="41"/>
      <line x1="0" y1="322" x2="407" y2="322"/>
      <line x1="0" y1="706" x2="407" y2="706"/>
      <line x1="0" y1="967" x2="407" y2="967"/>
      <line x1="393" y1="41" x2="393" y2="447"/>
      <line x1="22" y1="565" x2="22" y2="975"/>
    </g>
  </svg>

  <h1 class="brand">Mira Lune<br>Beauty Center</h1>

  <div class="photo-frame">space for digital photo frame</div>

  <div class="ornament" role="img" aria-label="Flowing floral swirl ornament in soft olive tones"></div>

  <ul class="services">
    <li>Aromatic Body Massage</li>
    <li>Aromatic Body Scrub / Polish</li>
    <li>Foot Reflexology</li>
    <li>Neck / Shoulder / Back Massage</li>
    <li>Facials</li>
    <li>Depilation</li>
    <li>Scalp Care</li>
    <li>Ear Candling</li>
  </ul>

  <p class="phone">Tel: 64187205</p>
</main>
</body>
</html>
```